Quenda-Ro Flyer (Business Launch)

Using my existing log design for Quenda-Ro Mobile Mechanics, I would like a flyer designed. This would be used for advertising, letterbox drops, handing to the public , door knocking ect.

I'm looking for clean cut simple though with the wow factor, I was thinking of even having the flyer in the shape of a van to promote that I'm a mobile business (I come to you ect)

I've attached copies of my logo and business cards.

I would like the following list of services we provide listed on the flyer (see back of business card).
7 day service (we come to you)
10% discount for online/email booking-enquiry

I think this should be enough for now.

I'm launching this business to aiming to hit the ground running,

Target Market(s)

All motor vehicle owners, house holds, businesses

Industry/Entity Type

Automotive

Font styles to use
Sans Serif
Other font styles liked:
• refer images

Colors
0355a3

Requirements
Must have
• services offered, logo, 7 days, we come to or or catchy phrase to let people know this.
• 10% discount for online/email booking enquiries
• Maintenance Package Servicing from $149 conditions apply
• my preference is for blue, grey and while colour scheme, though also happy to accept artistic design ideas to these.
Nice to have
• Wow factor, brochure that stand out from the rest
• Different share brochure in shape of work van (refer velkaro tramix van)
Should not have
• Not looking for a cheap quick fix, I'm wanting to create a brand .

```html
<!DOCTYPE html>
<html lang="en">
<head>
<meta charset="utf-8">
<title>Quenda-Ro Mobile Mechanics – Card</title>
<link rel="stylesheet" href="https://fonts.googleapis.com/css2?family=Roboto+Condensed:wght@400;700&display=swap">
<style>
  :root {
    --backdrop: #e6e6e6;
    --brand-blue: #0454a3;
    --mid-blue: #2e63b8;
    --brand-yellow: #f7e600;
    --panel-grey: #929292;
    --dark-grey: #7a7a7a;
    --ink: #1d1d1d;
    --logo-ink: #333333;
    --title-blue: #3557b0;
    --white: #ffffff;
  }
  html, body {
    margin: 0;
    padding: 0;
    width: 1200px;
    height: 960px;
    overflow: hidden;
    background: var(--backdrop);
    font-family: "Roboto Condensed", "Arial Narrow", sans-serif;
  }
  .stage { position: relative; width: 1200px; height: 960px; }
  .card { position: absolute; top: 227px; height: 505px; display: block; }
  .card--front { left: 184px; width: 390px; }
  .card--back { left: 627px; width: 387px; }
  .card text { font-family: "Roboto Condensed", "Arial Narrow", sans-serif; }
  .holder-name { fill: var(--ink); font-size: 31px; }
  .holder-role { fill: var(--title-blue); font-size: 20px; }
  .brand-name { fill: var(--logo-ink); font-size: 21px; font-weight: 700; }
  .contact-line { fill: var(--white); font-size: 20px; }
  .service-line { fill: var(--white); font-size: 27px; }
  .offer-line { fill: var(--brand-yellow); font-size: 22px; font-weight: 700; }
  .offer-note { fill: var(--white); font-size: 15px; }
  .abn-line { fill: var(--brand-blue); font-size: 27px; }
</style>
</head>
<body>
<main class="stage">

  <svg class="card card--front" viewBox="0 0 487 631" xmlns="http://www.w3.org/2000/svg">
    <defs>
      <linearGradient id="photo-tones" x1="0" y1="0" x2="1" y2="1">
        <stop offset="0" stop-color="#c9b15a"/>
        <stop offset="0.45" stop-color="#d9b843"/>
        <stop offset="0.75" stop-color="#3a6fc4"/>
        <stop offset="1" stop-color="#2b5aa8"/>
      </linearGradient>
    </defs>

    <rect class="panel-grey" x="0" y="0" width="487" height="631" fill="var(--panel-grey)"/>

    <rect class="photo-area" x="18" y="231" width="469" height="400" fill="url(#photo-tones)"
          role="img" aria-label="Photo: smiling mechanic in a blue cap and polo holding a clipboard in front of a yellow van"/>

    <polygon class="accent-stripe" points="200,0 210,0 487,426 487,441" fill="var(--dark-grey)"/>
    <polygon class="accent-yellow" points="210,0 487,0 487,426" fill="var(--brand-yellow)"/>
    <polygon class="accent-blue" points="0,206 270,631 0,631" fill="var(--mid-blue)"/>

    <text class="holder-name" x="128" y="122" text-anchor="middle">Darren Whitcombe</text>
    <text class="holder-role" x="128" y="153" text-anchor="middle">PRINCIPAL</text>

    <g class="brand">
      <circle cx="336" cy="77" r="16" fill="var(--brand-blue)"/>
      <text class="brand-name" x="358" y="84">Quenda-Ro</text>
    </g>

    <g class="contacts">
      <circle cx="32" cy="483" r="12" fill="var(--brand-yellow)"/>
      <path d="M26 486 q6 -9 12 0 v2 h-12 z" fill="var(--brand-blue)"/>
      <text class="contact-line" x="57" y="490">1300 482 716</text>

      <circle cx="32" cy="517" r="12" fill="var(--brand-yellow)"/>
      <rect x="28" y="510" width="8" height="14" rx="1.5" fill="none" stroke="var(--brand-blue)" stroke-width="1.6"/>
      <text class="contact-line" x="57" y="525">0412 587 309</text>

      <circle cx="32" cy="552" r="12" fill="var(--brand-yellow)"/>
      <text x="32" y="556" text-anchor="middle" font-size="11" fill="var(--brand-blue)">@</text>
      <text class="contact-line" x="57" y="559">admin@quenda-ro.com.au</text>

      <circle cx="32" cy="587" r="12" fill="var(--brand-yellow)"/>
      <circle cx="32" cy="587" r="6" fill="none" stroke="var(--brand-blue)" stroke-width="1.4"/>
      <line x1="26" y1="587" x2="38" y2="587" stroke="var(--brand-blue)" stroke-width="1.2"/>
      <text class="contact-line" x="57" y="594">www.quenda-ro.com.au</text>
    </g>
  </svg>

  <svg class="card card--back" viewBox="0 0 484 631" xmlns="http://www.w3.org/2000/svg">
    <rect x="0" y="0" width="484" height="631" fill="var(--brand-blue)"/>
    <polygon class="top-band" points="0,0 484,0 484,72 418,117 246,48 0,48" fill="var(--brand-yellow)"/>
    <rect class="bottom-band" x="0" y="583" width="484" height="48" fill="var(--brand-yellow)"/>

    <g class="service-list" text-anchor="middle">
      <text class="service-line" x="242" y="180">MOBILE SERVICE</text>
      <text class="service-line" x="242" y="213">7 DAYS A WEEK</text>
      <text class="service-line" x="242" y="262">Servicing and Repairs</text>
      <text class="service-line" x="242" y="314">Manufacturers</text>
      <text class="service-line" x="242" y="347">Log Book Service</text>
      <text class="service-line" x="242" y="399">Maintenance</text>
      <text class="service-line" x="242" y="432">Package Service from $149*</text>
      <text class="service-line" x="242" y="481">Pre-Purchase Inspections</text>
    </g>

    <g class="offer" text-anchor="middle">
      <text class="offer-line" x="242" y="527">10% OFF ONLINE / EMAIL BOOKINGS</text>
      <text class="offer-note" x="242" y="558">*Conditions apply</text>
    </g>

    <text class="abn-line" x="242" y="617" text-anchor="middle">ABN 48 615 930 472</text>
  </svg>

</main>
</body>
</html>
```